Business cards for Volibra employment termination service
Volibra
Wow! I am overwhelmed by how good these all look! It is very difficult to eliminate or rate any of them--they all look great!
Hello: Not sure what happened, but we need to also have "Bismarck, ND 58719" under the PO Box number.
Thanks,
RJD

```html
<!DOCTYPE html>
<html lang="en">
<head>
<meta charset="utf-8">
<title>Volibra Stationery</title>
<link href="https://fonts.googleapis.com/css2?family=Montserrat:wght@400;700&display=swap" rel="stylesheet">
<style>
:root{
  --teal:#1bbfb0;
  --orange:#f7a532;
  --paper:#ffffff;
  --ink:#6d6d6d;
  --stage:#ece7df;
  --label:#5a4f44;
}
*{box-sizing:border-box;margin:0;padding:0}
html,body{width:1200px;height:446px;overflow:hidden}
body{background:var(--stage);font-family:'Montserrat',sans-serif;position:relative}
.sheet{position:absolute;background:var(--paper);box-shadow:0 2px 6px rgba(0,0,0,.18);overflow:hidden}
.brand{display:flex;align-items:center;gap:4px;font-weight:700;color:var(--teal);position:absolute}
.brand-mark{background:var(--orange);display:block}
.wave{position:absolute;left:0;bottom:0;width:100%}
.label{position:absolute;font-size:7px;letter-spacing:1px;color:var(--label);text-align:center}
.tiny{font-size:4.5px;line-height:1.5;color:var(--ink);position:absolute}
.ghost{position:absolute;font-weight:700;color:var(--teal);opacity:.07;text-align:center;width:100%}

/* business cards */
.card{width:120px;height:48px}
.card-front{left:19px;top:168px}
.card-back{left:19px;top:252px}
.card-front .brand{left:8px;top:14px;font-size:9px}
.card-front .brand-mark{width:7px;height:7px}
.card-back .brand{left:8px;top:6px;font-size:7px}
.card-back .brand-mark{width:5px;height:5px}

/* letterheads */
.letterhead{width:293px;height:384px;top:12px}
.lh-one{left:163px}
.lh-two{left:475px}
.letterhead .brand{left:50%;transform:translateX(-50%);top:28px;font-size:14px}
.letterhead .brand-mark{width:10px;height:10px}
.letterhead .ghost{top:150px;font-size:44px}
.lh-one .tiny{right:16px;top:14px;text-align:right}
.lh-two .tiny{left:0;width:100%;text-align:center;bottom:40px}

/* envelopes */
.env-flap{left:826px;top:0;width:374px;height:232px;background:var(--paper)}
.env-flap .band{position:absolute;left:0;width:100%}
.env-flap .orange-band{top:0;height:40px;background:var(--orange)}
.env-flap .teal-band{top:40px;height:60px;background:var(--teal);clip-path:polygon(0 0,100% 0,100% 20%,50% 100%,0 20%)}
.env-flap .brand{left:50%;transform:translateX(-50%);top:150px;font-size:12px}
.env-flap .brand-mark{width:8px;height:8px}
.env-front{left:800px;top:269px;width:256px;height:139px}
.env-front .brand{left:10px;top:10px;font-size:9px}
.env-front .brand-mark{width:6px;height:6px}
.env-front .tiny{left:10px;top:24px}
</style>
</head>
<body>

<div class="sheet card card-front">
  <div class="brand"><span class="brand-mark"></span>Volibra</div>
  <svg class="wave" viewBox="0 0 120 14" height="14" preserveAspectRatio="none">
    <path d="M0 8 Q40 0 120 6 L120 14 L0 14Z" fill="var(--orange)"/>
    <path d="M0 10 Q50 3 120 10 L120 14 L0 14Z" fill="var(--teal)"/>
  </svg>
</div>
<div class="label" style="left:19px;top:220px;width:120px">Business Card Front</div>

<div class="sheet card card-back">
  <div class="brand"><span class="brand-mark"></span>Volibra</div>
  <div class="tiny" style="left:8px;top:17px">Rhea J. Dunmore · Director<br>701.555.0142<br>rjd@volibra.com</div>
  <svg class="wave" viewBox="0 0 120 10" height="10" preserveAspectRatio="none">
    <path d="M0 6 Q60 0 120 5 L120 10 L0 10Z" fill="var(--teal)"/>
  </svg>
</div>
<div class="label" style="left:19px;top:304px;width:120px">Business Card Back</div>

<div class="sheet letterhead lh-one">
  <div class="tiny">PO Box 412<br>Bismarck, ND 58719<br>701.555.0142<br>www.volibra.com</div>
  <div class="brand"><span class="brand-mark"></span>Volibra</div>
  <div class="ghost">Volibra</div>
  <svg class="wave" viewBox="0 0 293 40" height="40" preserveAspectRatio="none">
    <path d="M0 22 Q120 0 293 18 L293 40 L0 40Z" fill="var(--orange)"/>
    <path d="M0 28 Q150 8 293 26 L293 40 L0 40Z" fill="var(--teal)"/>
    <path d="M0 33 Q150 20 293 33 L293 40 L0 40Z" fill="var(--paper)"/>
  </svg>
</div>
<div class="label" style="left:163px;top:420px;width:293px">Letterhead Option 1</div>

<div class="sheet letterhead lh-two">
  <div class="brand"><span class="brand-mark"></span>Volibra</div>
  <div class="ghost">Volibra</div>
  <div class="tiny">PO Box 412 · Bismarck, ND 58719 · 701.555.0142 · www.volibra.com</div>
  <svg class="wave" viewBox="0 0 293 36" height="36" preserveAspectRatio="none">
    <path d="M0 20 Q150 0 293 16 L293 36 L0 36Z" fill="var(--teal)"/>
    <path d="M0 26 Q150 12 293 24 L293 36 L0 36Z" fill="var(--orange)"/>
    <path d="M0 31 Q150 22 293 31 L293 36 L0 36Z" fill="var(--paper)"/>
  </svg>
</div>
<div class="label" style="left:475px;top:420px;width:293px">Letterhead Option 2</div>

<div class="sheet env-flap">
  <div class="band orange-band"></div>
  <div class="band teal-band"></div>
  <div class="brand"><span class="brand-mark"></span>Volibra</div>
</div>

<div class="sheet env-front">
  <div class="brand"><span class="brand-mark"></span>Volibra</div>
  <div class="tiny">PO Box 412<br>Bismarck, ND 58719</div>
  <svg class="wave" viewBox="0 0 256 24" height="24" preserveAspectRatio="none">
    <path d="M0 12 Q110 0 256 10 L256 24 L0 24Z" fill="var(--orange)"/>
    <path d="M0 16 Q130 5 256 15 L256 24 L0 24Z" fill="var(--teal)"/>
  </svg>
</div>
<div class="label" style="left:800px;top:420px;width:256px">Envelope Option 3</div>

</body>
</html>
```